Vehicle wrap

To design a vehicle wrap using supplied company logo and photograph of vehicle.Design is for a spray painting company who spray on a wide variety of materails and objects. Design should be eyecatching and reflect the spary painting theme. Copy of a prevoius completed project included which is not as extensive as this project

Reason: Designs recieved so far are not working

Reason: End user has to make a decision

Target Market(s)

Motor vehicle audience as well as home renovators

Industry/Entity Type

Painting

Requirements
Must have
• Must have a logo which will be supplied and statement "We Coat It All * motor cycle tanks * kitchen splashbacks* Kitchens* car re-sprays

```html
<!DOCTYPE html>
<html lang="en">
<head>
<meta charset="utf-8">
<title>Glossrun Vehicle Wrap</title>
<link href="https://fonts.googleapis.com/css2?family=Archivo:wght@600;800&display=swap" rel="stylesheet">
<style>
  :root {
    --canvas: #ffffff;
    --wrap-blue: #3a5aa8;
    --wrap-green: #58a85a;
    --wrap-warm: #e6a23a;
    --plate: #3a3a3e;
    --ink: #111111;
    --text-light: #ffffff;
  }
  * { margin: 0; padding: 0; box-sizing: border-box; }
  html, body { width: 1200px; height: 1200px; overflow: hidden; background: var(--canvas); }
  .canvas { position: relative; width: 1200px; height: 1200px; background: var(--canvas); font-family: "Archivo", Arial, sans-serif; }

  .wrap-panel { position: absolute; }
  .wrap-fill {
    position: absolute; inset: 0; border-radius: inherit;
    background: linear-gradient(90deg, var(--wrap-blue) 0%, var(--wrap-green) 30%, var(--wrap-warm) 50%, var(--wrap-green) 70%, var(--wrap-blue) 100%);
  }

  /* Rear doors panel */
  .rear-wrap { left: 128px; top: 135px; width: 360px; height: 300px; border-radius: 36px 36px 8px 8px; }
  .rear-window { position: absolute; top: 30px; width: 138px; height: 138px; background: var(--plate); border-radius: 6px; }
  .rear-window--left { left: 30px; display: flex; align-items: center; justify-content: center; }
  .rear-window--right { left: 190px; padding: 16px 10px; }
  .rear-brand { color: var(--text-light); font-size: 21px; font-weight: 800; }

  /* Side panel */
  .side-wrap { left: 172px; top: 636px; width: 440px; height: 347px; border-radius: 56px 28px 8px 20px; }
  .brand-plate { position: absolute; left: 68px; top: 36px; width: 342px; height: 116px; background: var(--plate); border-radius: 6px; display: flex; align-items: center; justify-content: center; }
  .side-brand { color: var(--text-light); font-size: 54px; font-weight: 800; letter-spacing: 1px; line-height: 1; }

  .tagline { font-weight: 800; color: var(--ink); line-height: 1; }
  .side-wrap .tagline { position: absolute; left: 22px; top: 178px; font-size: 26px; }
  .rear-window .tagline { font-size: 15px; color: var(--text-light); margin-bottom: 8px; }

  .services { list-style: none; font-weight: 600; }
  .services li { display: flex; align-items: center; gap: 5px; }
  .services li::before { content: ""; width: 0; height: 0; border-left: 6px solid currentColor; border-top: 4px solid transparent; border-bottom: 4px solid transparent; }
  .side-wrap .services { position: absolute; left: 212px; top: 214px; color: var(--ink); font-size: 14px; line-height: 18px; }
  .rear-window .services { color: var(--text-light); font-size: 11px; line-height: 15px; }
</style>
</head>
<body>
<main class="canvas">
  <section class="wrap-panel rear-wrap" aria-label="Rear door wrap">
    <div class="wrap-fill" role="img" aria-label="Colour spectrum spray background"></div>
    <div class="rear-window rear-window--left">
      <span class="rear-brand">GLOSSRUN</span>
    </div>
    <div class="rear-window rear-window--right">
      <p class="tagline">We Coat It All</p>
      <ul class="services">
        <li>Motorcycle Tanks</li>
        <li>Glass Splashbacks</li>
        <li>Kitchens</li>
        <li>Car Re-sprays</li>
      </ul>
    </div>
  </section>

  <section class="wrap-panel side-wrap" aria-label="Side panel wrap">
    <div class="wrap-fill" role="img" aria-label="Colour spectrum spray background"></div>
    <div class="brand-plate">
      <span class="side-brand">GLOSSRUN</span>
    </div>
    <p class="tagline">We Coat It All</p>
    <ul class="services">
      <li>Motorcycle Tanks</li>
      <li>Glass Splashbacks</li>
      <li>Kitchens</li>
      <li>Car Re-sprays</li>
    </ul>
  </section>
</main>
</body>
</html>
```